Velisa Seafood Shipping Packaging Re-Design

We need a packaging (Shipping Carton) design for our Seafood Products (FROZEN). We already have a basic packaging design which we prefer to have a modern touch on it.
Spec :
1. It must show our logo (Attached), note that the text of "VELISA" which accompany the logo is optional, it can be omitted & showing only the logo.
2. Main color is Blue
3. Our carton is regular shipping box with dimension L43cm x W 27cm x H 16cm.
4. Our material of Carton is both Brown & White Kraft Paperboard, so the design should look nice in both material.

Attached our Logo and packaging design.

Target Market(s)

Frozen Seafood Distributor & Seafood Buyer

Industry/Entity Type

Food Production

Requirements
Must have
• 1. Must Show our Logo
• 2. Main Color of the Text/Logo is Blue
• 3. On the side of the packaging / Carton must show two box of CODE & SIZE
• 4. Must Show these icons :
• a. Handle with Care
• b. Maximum Stackable 10 Carton
• c. Recyleable Material
• d. Protect from the Water/Rain
Nice to have
• Would prefer to have a modern design

```html
<!DOCTYPE html>
<html lang="en">
<head>
<meta charset="utf-8">
<title>Velisa Frozen Seafood Shipping Carton – Dieline</title>
<link href="https://fonts.googleapis.com/css2?family=Lato:wght@400;700;900&display=swap" rel="stylesheet">
<style>
  :root{
    --navy:#1d3468;
    --blue:#0c5a9c;
    --mid:#1f7cb8;
    --light:#4aaed6;
    --pale:#a8d6ee;
    --ice:#cfe7f4;
    --white:#ffffff;
    --line:#8c9aa8;
  }
  *{margin:0;padding:0;box-sizing:border-box}
  html,body{width:1200px;height:1000px;overflow:hidden;background:var(--white)}
  body{position:relative;font-family:"Lato",sans-serif}

  .dieline{position:absolute;left:0;top:0;width:1200px;height:430px}
  .panel{position:absolute;overflow:hidden;border:1px solid var(--line)}
  .flipped{transform:rotate(180deg)}

  .glue-tab{position:absolute;left:28px;top:162px;width:28px;height:127px}

  /* panel surfaces */
  .face-logo{background:linear-gradient(to bottom,var(--navy) 0%,var(--blue) 100%)}
  .face-cold{background:linear-gradient(to bottom,#17417d 0%,var(--blue) 100%)}
  .face-side{background:linear-gradient(to bottom,var(--blue) 0%,var(--light) 100%)}
  .face-white{background:var(--white)}

  .flap-strip{position:absolute;left:0;top:0;width:100%;height:10px;background:var(--pale)}

  .frost-pattern{position:absolute;inset:0;background:radial-gradient(ellipse at 60% 50%,rgba(120,160,210,.22),rgba(120,160,210,0) 70%)}

  /* brand name */
  .brand{position:absolute;display:flex;flex-direction:column;align-items:center;color:var(--navy);font-weight:700}
  .brand .mark{border-radius:50%;background:var(--light)}
  .brand-main{left:50%;top:14px;transform:translateX(-50%)}
  .brand-main .mark{width:62px;height:62px;margin-bottom:10px}
  .brand-main .name{font-size:28px;letter-spacing:4px;line-height:1}
  .brand-small{left:50%;top:50%;transform:translate(-50%,-50%);color:var(--white)}
  .brand-small .mark{width:30px;height:30px;background:var(--pale);margin-bottom:4px}
  .brand-small .name{font-size:11px;letter-spacing:2px;line-height:1}

  /* label boxes */
  .label-box{position:absolute;border:1px solid var(--pale)}
  .label-box .tag{height:19px;border-bottom:1px solid var(--pale);color:var(--white);font-weight:900;font-size:13px;letter-spacing:1.5px;text-align:center;line-height:18px}
  .info-box{position:absolute;border:1px solid var(--pale)}
  .info-box .divider{position:absolute;left:0;right:0;top:50%;border-top:1px solid var(--pale)}

  /* thermometer */
  .thermo{position:absolute;width:32px;height:82px}

  /* care icons */
  .care-icons{position:absolute;left:20px;top:43px;display:flex;gap:11px}
  .care-icon{width:35px;height:35px;border:1px solid var(--pale);border-radius:2px;display:flex;align-items:center;justify-content:center}
</style>
</head>
<body>
<div class="dieline">

  <svg class="glue-tab" viewBox="0 0 28 127" aria-hidden="true">
    <polygon points="28,0 0,10 0,117 28,127" fill="#a8d6ee" stroke="#8c9aa8" stroke-width="1"/>
  </svg>

  <!-- top row (upside-down flaps) -->
  <div class="panel face-logo" style="left:55px;top:34px;width:340px;height:128px">
    <div class="flipped" style="position:absolute;inset:0">
      <div class="brand brand-small"><span class="mark"></span><span class="name">VELISA</span></div>
    </div>
    <div class="flap-strip"></div>
  </div>

  <div class="panel face-side" style="left:397px;top:34px;width:216px;height:128px">
    <div class="flipped" style="position:absolute;inset:0">
      <div class="label-box" style="left:11px;top:22px;width:90px;height:82px"><div class="tag">CODE</div></div>
      <div class="label-box" style="left:114px;top:22px;width:90px;height:82px"><div class="tag">SIZE</div></div>
    </div>
  </div>

  <div class="panel face-cold" style="left:615px;top:34px;width:341px;height:128px">
    <div class="flipped" style="position:absolute;inset:0">
      <div class="frost-pattern" role="img" aria-label="Faint snowflake pattern"></div>
      <svg class="thermo" style="left:15px;top:22px" viewBox="0 0 32 82" aria-label="Thermometer at minus 18 degrees">
        <rect x="8" y="1" width="16" height="62" rx="8" fill="#cfe7f4"/>
        <circle cx="16" cy="66" r="15" fill="#cfe7f4"/>
        <circle cx="16" cy="66" r="11" fill="#1f7cb8"/>
        <text x="16" y="68.5" font-family="Lato,sans-serif" font-size="6.5" font-weight="700" fill="#fff" text-anchor="middle">-18°C</text>
      </svg>
      <div class="info-box" style="left:197px;top:12px;width:128px;height:98px"><div class="divider"></div></div>
    </div>
    <div class="flap-strip"></div>
  </div>

  <div class="panel face-side" style="left:958px;top:34px;width:215px;height:128px">
    <div class="flipped" style="position:absolute;inset:0" id="icons-top">
      <div class="care-icons">
        <div class="care-icon"><svg width="24" height="24" viewBox="0 0 24 24" aria-label="Keep dry"><path d="M3 12a9 8 0 0 1 18 0z" fill="#fff"/><path d="M12 12v7a2 2 0 0 1-4 0" fill="none" stroke="#fff" stroke-width="1.6"/><path d="M5 5l-1-2M12 3V1M19 5l1-2" stroke="#fff" stroke-width="1.2"/></svg></div>
        <div class="care-icon"><svg width="24" height="24" viewBox="0 0 24 24" aria-label="Handle with care"><rect x="9" y="4" width="6" height="8" fill="#fff"/><path d="M3 8l5 8v5h3v-5M21 8l-5 8v5h-3" fill="none" stroke="#fff" stroke-width="2"/></svg></div>
        <div class="care-icon"><svg width="24" height="24" viewBox="0 0 24 24" aria-label="Stack limit 10"><text x="12" y="13" font-family="Lato,sans-serif" font-size="11" font-weight="700" fill="#fff" text-anchor="middle">10</text><path d="M4 16h16M4 19h16M4 22h16" stroke="#fff" stroke-width="1.4"/></svg></div>
        <div class="care-icon"><svg width="24" height="24" viewBox="0 0 24 24" aria-label="Recyclable"><path d="M12 3l4 7h-3M8 21H4l3-6M20 15l2 4-6 1" fill="none" stroke="#fff" stroke-width="2" stroke-linejoin="round"/><path d="M10 5L6 12M17 13l-3 6M5 17" fill="none" stroke="#fff" stroke-width="2"/></svg></div>
      </div>
    </div>
  </div>

  <!-- middle row (main faces) -->
  <div class="panel face-white" style="left:55px;top:162px;width:340px;height:128px">
    <div class="brand brand-main"><span class="mark"></span><span class="name">VELISA</span></div>
  </div>
  <div class="panel face-white" style="left:397px;top:162px;width:216px;height:128px"></div>
  <div class="panel face-white" style="left:615px;top:162px;width:341px;height:128px">
    <div class="brand brand-main"><span class="mark"></span><span class="name">VELISA</span></div>
  </div>
  <div class="panel face-white" style="left:958px;top:162px;width:215px;height:128px"></div>

  <!-- bottom row -->
  <div class="panel face-cold" style="left:55px;top:290px;width:340px;height:127px">
    <div class="frost-pattern" role="img" aria-label="Faint snowflake pattern"></div>
    <svg class="thermo" style="left:14px;top:22px" viewBox="0 0 32 82" aria-label="Thermometer at minus 18 degrees">
      <rect x="8" y="1" width="16" height="62" rx="8" fill="#cfe7f4"/>
      <circle cx="16" cy="66" r="15" fill="#cfe7f4"/>
      <circle cx="16" cy="66" r="11" fill="#1f7cb8"/>
      <text x="16" y="68.5" font-family="Lato,sans-serif" font-size="6.5" font-weight="700" fill="#fff" text-anchor="middle">-18°C</text>
    </svg>
    <div class="info-box" style="left:197px;top:12px;width:128px;height:98px"><div class="divider"></div></div>
  </div>

  <div class="panel face-side" style="left:397px;top:290px;width:216px;height:127px">
    <div class="care-icons">
      <div class="care-icon"><svg width="24" height="24" viewBox="0 0 24 24" aria-label="Keep dry"><path d="M3 12a9 8 0 0 1 18 0z" fill="#fff"/><path d="M12 12v7a2 2 0 0 1-4 0" fill="none" stroke="#fff" stroke-width="1.6"/><path d="M5 5l-1-2M12 3V1M19 5l1-2" stroke="#fff" stroke-width="1.2"/></svg></div>
      <div class="care-icon"><svg width="24" height="24" viewBox="0 0 24 24" aria-label="Handle with care"><rect x="9" y="4" width="6" height="8" fill="#fff"/><path d="M3 8l5 8v5h3v-5M21 8l-5 8v5h-3" fill="none" stroke="#fff" stroke-width="2"/></svg></div>
      <div class="care-icon"><svg width="24" height="24" viewBox="0 0 24 24" aria-label="Stack limit 10"><text x="12" y="13" font-family="Lato,sans-serif" font-size="11" font-weight="700" fill="#fff" text-anchor="middle">10</text><path d="M4 16h16M4 19h16M4 22h16" stroke="#fff" stroke-width="1.4"/></svg></div>
      <div class="care-icon"><svg width="24" height="24" viewBox="0 0 24 24" aria-label="Recyclable"><path d="M12 3l4 7h-3M8 21H4l3-6M20 15l2 4-6 1" fill="none" stroke="#fff" stroke-width="2" stroke-linejoin="round"/><path d="M10 5L6 12M17 13l-3 6" fill="none" stroke="#fff" stroke-width="2"/></svg></div>
    </div>
  </div>

  <div class="panel face-logo" style="left:615px;top:290px;width:341px;height:127px">
    <div class="brand brand-small"><span class="mark"></span><span class="name">VELISA</span></div>
  </div>

  <div class="panel face-side" style="left:958px;top:290px;width:215px;height:127px">
    <div class="label-box" style="left:11px;top:22px;width:90px;height:82px"><div class="tag">CODE</div></div>
    <div class="label-box" style="left:113px;top:22px;width:90px;height:82px"><div class="tag">SIZE</div></div>
  </div>

</div>
</body>
</html>
```